FenderPals Personal Injury Lawyers Website (Wordpress)

We need a brand new website for our firm's new rebranding. The name of the website is www.fenderpals-example.com. Our new brand will be a group of personal injury lawyers focused on representing only victims in car wrecks. We will be distinguishing ourselves from other law firms due to the fact that other law firms represent clients involving all forms of personal injury. We will only focus on car wrecks and this needs to be reflected on the website.

I have attached the new firm logo and stationary to show the designers the kind of look we are going for in the new website. It needs to be clean, pure, and show the potential clients that we only do one thing and we do it well. That thing is car wrecks.

Some examples of websites that we like are the following:
www.qvt-example.lu - nice interface and colors. nice navigation, we really like the biography pages for the individuals attorneys
www.morvantlegal-example.com - good layout, good navigation
www.pelliardwoss-example.com - navigation bar follows the user whether the user goes up or down

We would like five separate pages -- (1) Home, (2) Client Resources, (3) Expertise / Car Wrecks, (4) Contact Us, (5) News

The Home page will be used for driving traffic and should have a call to action on the right at the top stating that we will send an ebook to anyone who gives their contact information. The ebook will explain how car wrecks work. This should also have room for youtube videos which will be added later.

The client resources will include blogs, books, and information for potential clients. It should be presented in a well developed manner which is both appealing to potential and current clients.

The expertise page will show that we only focus on car wrecks. This needs to be a recurrent theme throughout the entire website. This page will focus on car wrecks and the different aspects including damages, insurance, and investigation.

The Contact Us page will show a google map to our address and phone number. Please use generic information and we will fill in the gaps upon the selection.

News: the news page will show different articles related to past and present cases and the successes of those clients.

The overall page should be elegant and creative. Do not include courthouses, gavels or anything else related to the law. If you include these things, your design will automatically be excluded.
Updates

Please take note this design is now guaranteed. I look forward to receiving everyone's wonderful designs.

Target Market(s)

Persons involved in car wrecks

Industry/Entity Type

Legal

Coding

Coded - Design and coding required

Number of Pages Required

5+ page

Font styles to use
Serif
Sans Serif

Colors
ec1f27
ffffff
000000

Requirements
Must have
• Five pages which focus on representation of car wreck victims. The site must be clean and easy to navigate.
Nice to have
• Navigation bar should follow user up and down the page.
Should not have
• Gavels, court houses, anything related to the law. If your design has these aspects, it will automatically be rejected

```html
<!DOCTYPE html>
<html lang="en">
<head>
<meta charset="utf-8">
<title>FenderPals – Expertise</title>
<link href="https://fonts.googleapis.com/css2?family=Open+Sans:wght@400;600;700;800&display=swap" rel="stylesheet">
<style>
:root{
  --red:#ec1f27;
  --blue:#2f8fe0;
  --blue-dark:#1f7bd0;
  --ink:#222;
  --muted:#666;
  --line:#e2e2e2;
  --panel:#f1f1f1;
  --topbar:#3a3a3a;
  --footer:#e9e9e9;
  --bottom:#333;
  --white:#fff;
}
*{box-sizing:border-box;margin:0;padding:0}
html,body{width:811px;height:1200px;overflow:hidden}
body{font-family:"Open Sans",Arial,sans-serif;color:var(--ink);background:var(--white);font-size:9px;line-height:1.5}
.topbar{height:26px;background:var(--topbar);color:#ddd;font-size:8px;display:flex;align-items:center;padding:0 62px;gap:16px}
.topbar span{display:flex;align-items:center;gap:4px}
.header{height:50px;display:flex;align-items:center;justify-content:space-between;padding:0 62px;border-bottom:1px solid var(--line)}
.brand{display:flex;align-items:center;gap:8px}
.brand-mark{width:14px;height:14px;background:var(--red);flex:none}
.brand-name{font-size:20px;font-weight:700;color:var(--ink);line-height:1}
.nav{display:flex;gap:2px}
.nav a{font-size:8px;color:#444;text-decoration:none;padding:4px 7px}
.nav a.active{background:var(--red);color:var(--white)}
.hero{height:309px;background:linear-gradient(180deg,var(--blue) 0%,var(--blue-dark) 100%);color:var(--white);text-align:center;padding-top:22px}
.hero h1{font-size:25px;font-weight:700;margin-bottom:12px}
.hero p{width:560px;margin:0 auto;font-size:8.5px;line-height:1.55}
.hero .lead-in{margin-top:12px}
.aspects{display:flex;justify-content:space-between;width:640px;margin:24px auto 0;text-align:left}
.aspect{display:flex;gap:10px;width:190px}
.aspect-icon{width:46px;height:46px;border-radius:50%;background:var(--white);flex:none;display:flex;align-items:center;justify-content:center}
.aspect h3{font-size:11px;font-weight:700;margin:4px 0 3px}
.aspect p{width:auto;font-size:8px;margin:0}
.cta{width:688px;margin:42px auto 0;height:128px;background:var(--panel);text-align:center;padding-top:20px}
.cta h2{font-size:22px;font-weight:700;color:#333;margin-bottom:8px}
.cta p{width:500px;margin:0 auto;font-size:8px;color:var(--muted)}
.cta .button{display:inline-block;margin-top:10px;background:var(--red);color:var(--white);font-size:7.5px;padding:4px 14px}
.testimonials{height:390px;padding-top:40px;text-align:center;background:linear-gradient(180deg,#fff 0%,#f3f8fc 55%,#e9f1f8 100%)}
.testimonials h2{font-size:22px;font-weight:700;color:#333}
.testimonials .intro{width:470px;margin:8px auto 0;font-size:8px;color:var(--muted)}
.quotes{display:flex;justify-content:space-between;width:560px;margin:42px auto 0}
.quote{width:150px}
.portrait{width:108px;height:108px;border-radius:50%;margin:0 auto;border:3px solid var(--white);box-shadow:0 0 0 1px #ddd;background:radial-gradient(circle at 50% 40%,#d9cfc6 0%,#b7aca3 55%,#8f8a86 100%)}
.quote p{font-size:8px;color:var(--muted);margin-top:14px}
.quote .who{margin-top:6px;font-style:italic;color:#444}
.quote .who b{font-weight:700}
.footer{height:220px;background:var(--footer);display:flex;justify-content:space-between;padding:22px 62px 0;border-top:1px solid #d8d8d8}
.footer-col{width:150px}
.footer-col h4{font-size:11px;font-weight:600;color:#444;text-transform:uppercase;margin-bottom:8px}
.footer-col ul{list-style:none}
.footer-col li{font-size:8px;color:#777;line-height:2}
.bottombar{height:35px;background:var(--bottom);color:#bbb;font-size:7.5px;display:flex;align-items:center;justify-content:space-between;padding:0 62px}
.bottombar nav{display:flex;gap:12px}
</style>
</head>
<body>
<div class="topbar">
  <span><svg width="8" height="8" viewBox="0 0 10 10"><path d="M2 1l2 2-1 1.5c.6 1.3 1.4 2.1 2.5 2.5L7 6l2 2-1.5 1.5C4.5 9 1 5.5.5 2.5z" fill="#ddd"/></svg>+1 (555) 014-2290</span>
  <span><svg width="9" height="7" viewBox="0 0 10 8"><rect x=".5" y=".5" width="9" height="7" fill="none" stroke="#ddd"/><path d="M.5 .5l4.5 4 4.5-4" fill="none" stroke="#ddd"/></svg>hello@fenderpals-example.com</span>
</div>

<header class="header">
  <div class="brand">
    <span class="brand-mark"></span>
    <span class="brand-name">FenderPals</span>
  </div>
  <nav class="nav">
    <a href="#">Home</a><a href="#">About Us</a><a href="#" class="active">Expertise</a><a href="#">Works Done</a><a href="#">Resources</a><a href="#">News</a><a href="#">Contact</a>
  </nav>
</header>

<section class="hero">
  <h1>We focus Only on Car Wrecks</h1>
  <p>We have a lot of experience and expertise on the section of Car Wrecks as we handle only these cases for our clients. And now it's easy to speak about us that we are the number one firm you can trust on this section. Lorem ipsum dolor sit amet, consectetur adipisicing elit, sed do eiusmod tempor incididunt ut labore et dolore magna aliqua. Ut enim ad minim veniam, quis nostrud exercitation ullamco laboris nisi ut aliquip ex ea commodo consequat duis aute irure dolor.</p>
  <p class="lead-in">The different aspects including in our Service/Expertise on this section are:</p>
  <div class="aspects">
    <div class="aspect">
      <div class="aspect-icon"><svg width="22" height="22" viewBox="0 0 22 22"><path d="M5 1v16h16M1 5h16v16" fill="none" stroke="#ec1f27" stroke-width="2.5"/></svg></div>
      <div><h3>Damages</h3><p>Lorem ipsum dolor sit amet, consectetur adipisicing elit.</p></div>
    </div>
    <div class="aspect">
      <div class="aspect-icon"><svg width="22" height="22" viewBox="0 0 22 22"><path d="M15 6c-1-1.5-7-2-7 1.5S16 10 16 14s-7 3.5-9 1.5M11 2v18" fill="none" stroke="#ec1f27" stroke-width="2.5"/></svg></div>
      <div><h3>Insurance</h3><p>Lorem ipsum dolor sit amet, consectetur adipisicing elit.</p></div>
    </div>
    <div class="aspect">
      <div class="aspect-icon"><svg width="22" height="22" viewBox="0 0 22 22"><circle cx="9" cy="9" r="6" fill="none" stroke="#ec1f27" stroke-width="2.5"/><path d="M13.5 13.5l6 6" stroke="#ec1f27" stroke-width="3"/></svg></div>
      <div><h3>Investigation</h3><p>Lorem ipsum dolor sit amet, consectetur adipisicing elit.</p></div>
    </div>
  </div>
</section>

<section class="cta">
  <h2>Ready to get started</h2>
  <p>Lorem ipsum dolor sit amet, consectetur adipisicing elit, sed do eiusmod tempor incididunt ut labore et dolore magna aliqua. Ut enim ad minim veniam quis nostrud exercitation ullamco laboris nisi ut aliquip.</p>
  <span class="button">Request a free Quote</span>
</section>

<section class="testimonials">
  <h2>What Clients say about our Expertise on Car Wrecks</h2>
  <p class="intro">Lorem ipsum dolor sit amet, consectetur adipisicing elit, sed do eiusmod tempor incididunt ut labore et dolore magna aliqua. Ut enim ad minim veniam quis nostrud.</p>
  <div class="quotes">
    <div class="quote">
      <div class="portrait" role="img" aria-label="Portrait photo of a client"></div>
      <p>Lorem ipsum dolor sit amet, consectetur adipisicing elit, sed do eiusmod tempor incididunt.</p>
      <p class="who"><b>John Doe</b> / Director of company</p>
    </div>
    <div class="quote">
      <div class="portrait" role="img" aria-label="Portrait photo of a client"></div>
      <p>Lorem ipsum dolor sit amet, consectetur adipisicing elit, sed do eiusmod tempor incididunt.</p>
      <p class="who"><b>John Doe</b> / Director of company</p>
    </div>
    <div class="quote">
      <div class="portrait" role="img" aria-label="Portrait photo of a client"></div>
      <p>Lorem ipsum dolor sit amet, consectetur adipisicing elit, sed do eiusmod tempor incididunt.</p>
      <p class="who"><b>John Doe</b> / Director of company</p>
    </div>
  </div>
</section>

<footer class="footer">
  <div class="footer-col"><h4>Company</h4><ul><li>About Us</li><li>Meet the team</li><li>Careers</li><li>Privacy policy</li><li>Contact us</li></ul></div>
  <div class="footer-col"><h4>Support</h4><ul><li>FAQ</li><li>Blog</li><li>Forums</li><li>Ticket system</li><li>Billing system</li></ul></div>
  <div class="footer-col"><h4>Necessary Links</h4><ul><li>Free ebook</li><li>Client resources</li><li>Car wrecks</li><li>News</li><li>Videos</li></ul></div>
  <div class="footer-col"><h4>Valued Partners</h4><ul><li>Partner one</li><li>Partner two</li><li>Partner three</li><li>Partner four</li><li>Partner five</li></ul></div>
</footer>

<div class="bottombar">
  <span>© 2013 FenderPals. All rights reserved.</span>
  <nav><span>Home</span><span>About Us</span><span>Faq</span><span>Contact Us</span></nav>
</div>
</body>
</html>
```